International Medical travel company needs professional card

We just purchased a logo through craft lantern, and now need a business card. We contract with Middle Eastern governments to bring patients who need complex medical care to the U.S. for treatment. We will upload logo. Titles, names, contact info, etc. needs to be in English on one side, Arabic on the other

Target Market(s)

Health administrators, professionals

Industry/Entity Type

Health Care

Contact Information for Business Card

logo on each side. Usual name/title/contact info

Font styles to use
Serif
Sans Serif

Colors
0255a3

Requirements
Must have
• English one side, Arabic the other

```html
<!DOCTYPE html>
<html lang="en">
<head>
<meta charset="utf-8">
<title>Meridian Care – Business Card</title>
<link rel="stylesheet" href="https://fonts.googleapis.com/css2?family=Tinos:wght@400;700&family=Noto+Naskh+Arabic:wght@400;700&display=swap">
<style>
  :root {
    --backdrop: #2b2b2b;
    --card-dark: #000000;
    --card-light: #ffffff;
    --gold: #c9b53a;
    --gold-deep: #a8952a;
    --blue: #0255a3;
  }
  * { box-sizing: border-box; margin: 0; padding: 0; }
  html, body {
    width: 1200px; height: 900px; overflow: hidden;
    background: var(--backdrop);
  }
  .stage {
    width: 1200px; height: 900px;
    display: flex; flex-direction: column; align-items: center; justify-content: center;
    gap: 52px;
  }
  .card {
    width: 660px; height: 377px;
    position: relative;
    box-shadow: 0 12px 30px rgba(0,0,0,.5);
  }
  .card--arabic { background: var(--card-dark); }
  .card--english { background: var(--card-light); }

  /* Brand block */
  .brand {
    position: absolute;
    display: flex; align-items: center; gap: 14px;
    font-family: "Tinos", serif; font-weight: 700;
    color: var(--gold);
  }
  .brand__square {
    width: 26px; height: 26px;
    border: 4px solid var(--gold);
    flex: none;
  }
  .card--arabic .brand { left: 52px; top: 158px; font-size: 40px; }
  .card--english .brand { left: 40px; top: 164px; font-size: 34px; }

  /* Arabic side details */
  .details-ar {
    position: absolute; right: 48px; top: 56px;
    direction: rtl; text-align: right;
    font-family: "Noto Naskh Arabic", serif;
    color: var(--gold);
  }
  .details-ar .person-name { font-size: 34px; font-weight: 700; line-height: 1.1; }
  .details-ar .person-title { font-size: 19px; color: var(--blue); margin-bottom: 10px; }
  .details-ar .address { font-size: 17px; line-height: 1.45; margin-bottom: 10px; }
  .details-ar .contact { font-family: "Tinos", serif; font-size: 18px; line-height: 1.5; }

  .contact-row { display: flex; align-items: center; gap: 10px; }
  .contact-row bdi { direction: ltr; unicode-bidi: isolate; }
  .icon { width: 14px; height: 14px; flex: none; }
  .icon path, .icon circle, .icon rect, .icon ellipse { stroke: var(--blue); fill: none; stroke-width: 1.6; }
  .card--english .icon path, .card--english .icon circle, .card--english .icon rect, .card--english .icon ellipse { stroke: var(--gold-deep); }

  /* English side */
  .divider {
    position: absolute; left: 318px; top: 70px;
    width: 2px; height: 230px;
    background: linear-gradient(var(--blue), rgba(2,85,163,0));
  }
  .details-en {
    position: absolute; left: 344px; top: 92px;
    font-family: "Tinos", serif; color: var(--blue);
  }
  .details-en .person-name { font-size: 27px; font-weight: 700; line-height: 1.1; }
  .details-en .person-title { font-size: 17px; color: var(--gold-deep); margin-bottom: 10px; }
  .details-en .address { font-size: 18px; line-height: 1.3; margin-bottom: 10px; }
  .details-en .contact { font-size: 18px; line-height: 1.4; }
</style>
</head>
<body>
<main class="stage">

  <section class="card card--arabic" lang="ar">
    <div class="brand"><span class="brand__square"></span>Meridian Care</div>
    <div class="details-ar">
      <p class="person-name">خالد رحمن</p>
      <p class="person-title">مدير</p>
      <p class="address">شارع النخيل، 21577<br>جدة، المملكة العربية السعودية</p>
      <div class="contact">
        <p class="contact-row">
          <svg class="icon" viewBox="0 0 16 16"><path d="M4 2l3 3-1.5 2a8 8 0 0 0 3.5 3.5L11 9l3 3-2 2C6 13 3 10 2 4z"/></svg>
          <bdi>+330 5182 -4706</bdi>
        </p>
        <p class="contact-row">
          <svg class="icon" viewBox="0 0 16 16"><rect x="2" y="4" width="12" height="8"/><path d="M2 4l6 5 6-5"/></svg>
          <bdi>info@meridiancare.com</bdi>
        </p>
        <p class="contact-row">
          <svg class="icon" viewBox="0 0 16 16"><circle cx="8" cy="8" r="6"/><ellipse cx="8" cy="8" rx="2.5" ry="6"/><path d="M2 8h12"/></svg>
          <bdi>www.meridiancare.com</bdi>
        </p>
      </div>
    </div>
  </section>

  <section class="card card--english">
    <div class="brand"><span class="brand__square"></span>Meridian Care</div>
    <div class="divider"></div>
    <div class="details-en">
      <p class="person-name">Khalid Rahman</p>
      <p class="person-title">Director</p>
      <p class="address">Palm Street, 21577<br>Jeddah, Saudi Arabia</p>
      <div class="contact">
        <p class="contact-row">
          <svg class="icon" viewBox="0 0 16 16"><path d="M4 2l3 3-1.5 2a8 8 0 0 0 3.5 3.5L11 9l3 3-2 2C6 13 3 10 2 4z"/></svg>
          +330 5182 -4706
        </p>
        <p class="contact-row">
          <svg class="icon" viewBox="0 0 16 16"><rect x="2" y="4" width="12" height="8"/><path d="M2 4l6 5 6-5"/></svg>
          info@meridiancare.com
        </p>
        <p class="contact-row">
          <svg class="icon" viewBox="0 0 16 16"><circle cx="8" cy="8" r="6"/><ellipse cx="8" cy="8" rx="2.5" ry="6"/><path d="M2 8h12"/></svg>
          www.meridiancare.com
        </p>
      </div>
    </div>
  </section>

</main>
</body>
</html>
```